Business Card Design Project

This design is a slimline business card 45mm x90mm, the card will be printed at 49mm x 94mm and cut to 45mm x90 mm, this needs to be considered in the design. The content required on the front and back of the business card is attached in a pdf; the design will be done using photo shop as we use CS6 in our business. The design needs to be developed using a CMYK colour pallet, the main colours used on our business are red, grey black and white. A snapshot of our business brochure and new website has been provided to give you an understanding on our businesses look and feel.
FRONT OF BUSINESS CARD
Director
Marcus Fenwick
Ph+61 0421780213
www.brightlanepartners.com.au
marcusfenwick@brightlanepartners.com.au
BACK OF BUSINESS CARD
SUPPORTING CLIENTS IN
Oil & Gas I Minerals & Metals I Petrochemical I Manufacturing
Building & Construction I Telecommunication I Rail I Civil I New Industries
KNOWLEDGE I EXPERTISE I EXPERIENCE I CAPACITY

```html
<!DOCTYPE html>
<html lang="en">
<head>
<meta charset="utf-8">
<title>Brightlane Partners – Business Card</title>
<link rel="stylesheet" href="https://fonts.googleapis.com/css2?family=Open+Sans:wght@400;600;700;800&display=swap">
<style>
  :root {
    --page: #e4e1dc;
    --card-black: #111111;
    --card-charcoal: #1d1d1d;
    --red: #c8102e;
    --red-dark: #8e0c1f;
    --white: #ffffff;
    --band-light: #f2f2f2;
    --band-grey: #c9c9c9;
    --text-dark: #1a1a1a;
    --text-grey: #6b6b6b;
  }
  * { box-sizing: border-box; margin: 0; padding: 0; }
  html, body {
    width: 1200px; height: 1200px; overflow: hidden;
    background: var(--page);
    font-family: "Open Sans", Arial, sans-serif;
  }
  .canvas { position: relative; width: 1200px; height: 1200px; }

  .card {
    position: absolute; left: 160px; width: 880px; height: 440px;
    background: radial-gradient(ellipse at 35% 30%, var(--card-charcoal), var(--card-black) 75%);
    box-shadow: 0 12px 30px rgba(0,0,0,.25);
    overflow: hidden;
  }
  .card--front { top: 100px; }
  .card--back { top: 660px; }

  .card__band {
    position: absolute; left: 0; right: 0; bottom: 0; height: 96px;
    background: linear-gradient(180deg, var(--band-light) 0%, var(--band-grey) 100%);
    border-top: 4px solid var(--red);
    box-shadow: 0 -5px 0 #2a2a2a;
  }

  /* Front */
  .identity { position: absolute; left: 70px; top: 64px; }
  .identity__name { font-size: 40px; font-weight: 600; color: var(--white); letter-spacing: .5px; }
  .identity__surname { color: var(--red); }
  .identity__role {
    margin-top: 8px; margin-left: 62px; font-size: 15px; font-weight: 700;
    letter-spacing: 2px; color: var(--white); text-transform: uppercase;
  }
  .contacts { position: absolute; left: 70px; top: 204px; list-style: none; }
  .contacts__item {
    display: flex; align-items: center; gap: 8px; margin-bottom: 17px;
    font-size: 15px; font-weight: 600; color: var(--white);
  }
  .contacts__icon {
    width: 20px; height: 20px; border-radius: 50%; background: var(--red);
    display: flex; align-items: center; justify-content: center;
    font-size: 11px; font-weight: 800; color: var(--white);
  }

  .brand { display: flex; flex-direction: column; }
  .brand__row { display: flex; align-items: center; gap: 8px; }
  .brand__mark { width: 14px; height: 14px; background: var(--red); }
  .brand__name { font-weight: 800; letter-spacing: .5px; text-transform: uppercase; }
  .brand__tagline { font-weight: 600; }

  .brand--band { position: absolute; right: 40px; top: 20px; align-items: flex-end; }
  .brand--band .brand__name { font-size: 28px; color: var(--text-dark); }
  .brand--band .brand__tagline { font-size: 9px; color: var(--text-dark); margin-top: 2px; }

  /* Back */
  .back-lockup {
    position: absolute; left: 60px; top: 140px; right: 40px;
    display: flex; align-items: center; gap: 22px;
  }
  .brand--dark .brand__name { font-size: 30px; color: var(--white); }
  .brand--dark .brand__tagline { font-size: 9px; color: var(--white); margin-top: 4px; margin-left: 22px; }
  .sectors {
    border-left: 2px solid var(--red); padding-left: 12px;
    list-style: none; font-size: 11px; font-weight: 600; color: var(--red); line-height: 1.7;
  }
  .values {
    position: absolute; left: 0; right: 0; top: 32px; text-align: center;
    font-size: 14px; font-weight: 800; color: var(--red-dark); letter-spacing: .5px;
  }
</style>
</head>
<body>
<main class="canvas">

  <section class="card card--front" aria-label="Business card front">
    <div class="identity">
      <h1 class="identity__name">Marcus <span class="identity__surname">Fenwick</span></h1>
      <p class="identity__role">Director</p>
    </div>
    <ul class="contacts">
      <li class="contacts__item"><span class="contacts__icon">P</span>: +61 0437925846</li>
      <li class="contacts__item"><span class="contacts__icon">E</span>: marcusfenwick@brightlanepartners.com.au</li>
      <li class="contacts__item"><span class="contacts__icon">W</span>: www.brightlanepartners.com.au</li>
    </ul>
    <div class="card__band">
      <div class="brand brand--band">
        <div class="brand__row"><span class="brand__mark"></span><span class="brand__name">Brightlane Partners</span></div>
        <span class="brand__tagline">Providing Effective Project Controls and Management Solutions</span>
      </div>
    </div>
  </section>

  <section class="card card--back" aria-label="Business card back">
    <div class="back-lockup">
      <div class="brand brand--dark">
        <div class="brand__row"><span class="brand__mark"></span><span class="brand__name">Brightlane Partners</span></div>
        <span class="brand__tagline">Providing Effective Project Controls and Management Solutions</span>
      </div>
      <ul class="sectors">
        <li>Oil &amp; Gas | Minerals &amp; Metals | Petrochemical</li>
        <li>Manufacturing | Building &amp; Construction</li>
        <li>Telecommunication | Rail | Civil | New Industries</li>
      </ul>
    </div>
    <div class="card__band">
      <p class="values">KNOWLEDGE | EXPERTISE | EXPERIENCE | CAPACITY</p>
    </div>
  </section>

</main>
</body>
</html>
```